Website Design for Cloudharborly As a Service

We are building a service to allow customers to own their own private clouds easily and cheaply. Owning your own private cloud saves costs, and offers more flexibility than a public cloud provider but has historically been a complex and expensive option.

We plan to offer a service where we build and maintain your own private cloud on your own hardware for a cheap monthly costs. Similar to this service - https://stackorra.com/solutions/private-cloud

We already have a logo and branding in place - we'd like a website design to be tailored from this branding, see attached logo design.

Feel free to add important elements on the home page such as testimonials, client/partner logos, contact form, social media, etc using placeholder contents in addition to the document we attached.

We also plan to add sub-pages in the future so please make sure that your website design has a full navigation menu.

An example of the site we like: https://www.verimoxa.com/ we'd be happy for you to take inspiration from this website.

Target Market(s)

B2B focused, we are targeting start-up/small/medium sized companies who needs help with their cloud and IT infrastructure.

Industry/Entity Type

IT

Number of Pages Required

1 page

Font styles to use
Other font styles liked:
• Please refer to the attachment - font must have Mayeka Demi Bold & Retroica

Requirements
Must have
• Please add placeholder menu since we're planning to have subpages later on.

```html
<!DOCTYPE html>
<html lang="en">
<head>
<meta charset="utf-8">
<title>Cloudharborly as a Service</title>
<link href="https://fonts.googleapis.com/css2?family=Lexend:wght@400;500;600&family=Questrial&display=swap" rel="stylesheet">
<style>
:root{
  --navy:#0a1d29;
  --orange:#f7931e;
  --blue:#1d86d6;
  --blue-light:#bcd8ec;
  --steel:#5b86a7;
  --ink:#1f2a33;
  --muted:#3a4650;
  --white:#ffffff;
  --line:#26394a;
}
*{margin:0;padding:0;box-sizing:border-box}
html,body{width:1200px;height:4914px;overflow:hidden;background:var(--white)}
body{position:relative;font-family:"Questrial",sans-serif;color:var(--ink)}
.abs{position:absolute}
h1,h2,h3,h4{font-family:"Lexend",sans-serif;font-weight:500}
.btn{position:absolute;display:flex;align-items:center;justify-content:center;background:var(--orange);color:var(--white);font-family:"Lexend",sans-serif;font-size:14px;text-decoration:none}
.accent{position:absolute;width:54px;height:4px;background:var(--orange)}

/* hero */
.hero{position:absolute;left:0;top:0;width:1200px;height:790px;background:var(--navy);clip-path:polygon(0 0,1200px 0,1200px 672px,0 790px)}
.logo{position:absolute;display:flex;align-items:center;gap:10px;font-family:"Lexend",sans-serif;font-size:24px;font-weight:500;color:var(--white)}
.logo .dot{width:22px;height:22px;border-radius:50%;background:var(--blue)}
.nav a{position:absolute;top:52px;color:var(--white);font-size:14px;text-decoration:none;font-family:"Lexend",sans-serif}
.nav a.active{color:var(--blue);border-bottom:1px solid var(--blue);padding-bottom:3px}
.caret{display:inline-block;margin-left:5px;border-left:4px solid transparent;border-right:4px solid transparent;border-top:5px solid var(--white);vertical-align:2px}
.hero h1{position:absolute;left:57px;top:176px;width:520px;font-size:40px;line-height:58px;font-weight:600;color:var(--white)}
.hero p{position:absolute;left:57px;top:437px;width:510px;font-size:15px;line-height:23px;color:var(--white)}
.art{position:absolute;border-radius:14px}

/* benefits */
.benefits h2{position:absolute;left:57px;top:910px;width:520px;font-size:39px;line-height:53px;color:var(--ink)}
.benefits p.lead{position:absolute;left:57px;top:1038px;width:520px;font-size:15px;line-height:23px;color:var(--muted)}
.card{position:absolute;width:250px;height:330px;background:var(--white);box-shadow:0 6px 28px rgba(10,29,41,.12);padding:30px 22px}
.card .ico{width:72px;height:72px;border-radius:50%;background:var(--orange);border:3px solid var(--navy)}
.card h3{margin-top:26px;font-size:19px;line-height:25px;color:var(--blue);font-weight:400}
.card p{margin-top:22px;font-size:15px;line-height:23px;color:var(--ink)}

/* transformation */
.transform{position:absolute;left:0;top:1620px;width:1200px;height:820px;background:var(--navy)}
.transform h2{position:absolute;left:57px;top:140px;width:540px;font-size:39px;line-height:53px;color:var(--white)}
.transform .copy{position:absolute;left:57px;top:323px;width:580px;font-size:15px;line-height:23px;color:var(--white)}
.transform .copy p{margin-bottom:10px}
.check{position:absolute;display:flex;align-items:center;gap:12px;font-family:"Lexend",sans-serif;font-size:23px;color:var(--white)}
.check svg{width:20px;height:20px}
.link{position:absolute;color:var(--orange);font-family:"Lexend",sans-serif;font-size:15px;text-decoration:underline;display:flex;align-items:center;gap:10px}

/* public cloud */
.public h2{position:absolute;left:57px;top:2562px;width:520px;font-size:39px;line-height:53px;color:var(--ink)}
.pcard{position:absolute;width:521px;background:var(--white);box-shadow:0 6px 28px rgba(10,29,41,.12);padding:28px 32px}
.pcard .head{display:flex;gap:14px;align-items:flex-start}
.pcard .pico{flex:none;width:40px;height:40px;border-radius:50%;background:var(--orange)}
.pcard .pico.blue{background:#6a5ad8}
.pcard .pico.green{background:#3aa64a}
.pcard h3{font-size:19px;line-height:25px;color:var(--blue);font-weight:400;padding-top:6px}
.pcard p{margin-top:12px;font-size:15px;line-height:23px;color:var(--ink)}
.outline{position:absolute;left:502px;top:3057px;width:194px;height:55px;border:2px solid var(--orange);color:var(--orange);display:flex;align-items:center;justify-content:center;font-family:"Lexend",sans-serif;font-size:16px}

/* different */
.diff{position:absolute;left:0;top:3215px;width:1200px;height:900px;background:var(--navy)}
.diff h2{position:absolute;left:57px;top:87px;width:480px;font-size:39px;line-height:53px;color:var(--white)}
.step{position:absolute;display:flex;align-items:center;gap:24px;width:460px}
.step .num{flex:none;width:66px;height:66px;border-radius:50%;border:2px dashed var(--blue);color:var(--blue);font-family:"Lexend",sans-serif;font-size:32px;display:flex;align-items:center;justify-content:center}
.step p{font-size:15px;line-height:23px;color:var(--white);width:370px}

/* newsletter */
.news h2{position:absolute;left:0;top:4140px;width:1200px;text-align:center;font-size:38px;color:var(--ink)}
.news .bar{position:absolute;left:542px;top:4134px;width:54px;height:4px;background:var(--orange)}
.news p{position:absolute;left:190px;top:4232px;width:820px;text-align:center;font-size:15px;line-height:23px;color:var(--ink)}
.field{position:absolute;left:250px;top:4302px;width:547px;height:55px;background:#f0f2f4;display:flex;align-items:center;padding-left:20px;font-size:14px;color:var(--muted)}

/* footer */
.footer{position:absolute;left:0;top:4484px;width:1200px;height:430px;background:var(--navy);color:var(--white)}
.footer .about{position:absolute;left:57px;top:150px;width:250px;font-size:15px;line-height:25px}
.social{position:absolute;top:290px;width:24px;height:24px;border-radius:50%;background:var(--white)}
.col{position:absolute;top:106px}
.col h4{font-size:16px;font-weight:500;margin-bottom:20px}
.col li{list-style:none;font-size:14px;line-height:26px}
.col .c{display:flex;align-items:center;gap:10px}
.col .c svg{width:12px;height:12px}
.rule{position:absolute;left:57px;top:343px;width:1084px;height:1px;background:var(--line)}
.copyright{position:absolute;left:57px;top:370px;font-size:15px;display:flex;align-items:center;gap:8px}
.legal{position:absolute;right:59px;top:370px;font-size:15px}
</style>
</head>
<body>

<header class="hero">
  <div class="logo" style="left:57px;top:45px"><span class="dot"></span>Cloudharborly</div>
  <nav class="nav">
    <a class="active" style="left:397px" href="#">Home</a>
    <a style="left:471px" href="#">Products<span class="caret"></span></a>
    <a style="left:570px" href="#">Solutions<span class="caret"></span></a>
    <a style="left:671px" href="#">Pricing</a>
    <a style="left:757px" href="#">About</a>
  </nav>
  <a class="btn" style="left:1000px;top:42px;width:141px;height:42px" href="#">Get Started</a>
  <h1>A Groundbreaking Way For Your Small Business To Benefit From The Power Of The Cloud</h1>
  <p>Cloudharborly as a Service is here to help small businesses utilise the power of the cloud without complicated set-ups or scary price tags<br>Ready to modernise your infrastructure with a fully</p>
  <a class="btn" style="left:57px;top:559px;width:162px;height:52px" href="#">Contact Us</a>
  <div class="art" role="img" aria-label="Isometric illustration of a blue server unit cabled up to a cloud" style="left:590px;top:205px;width:600px;height:470px;background:radial-gradient(ellipse at 35% 45%,#2f8fe0 0%,#1b5f9c 38%,rgba(10,29,41,0) 70%),radial-gradient(ellipse at 85% 25%,#d6ecfb 0%,rgba(10,29,41,0) 45%)"></div>
</header>

<section class="benefits">
  <div class="accent" style="left:57px;top:895px"></div>
  <h2>How Do We Benefit Your Business</h2>
  <p class="lead">Cloudharborly as a Service is here to help small businesses utilise the power of the cloud without complicated set-ups or scary price tags</p>
  <a class="btn" style="left:57px;top:1135px;width:174px;height:52px" href="#">Learn more</a>

  <article class="card" style="left:612px;top:910px"><div class="ico" role="img" aria-label="Fast cloud icon"></div><h3>Faster Cloud Solutions</h3><p>our private cloud solutions outpace public clouds</p></article>
  <article class="card" style="left:891px;top:910px"><div class="ico" role="img" aria-label="Flexible cloud icon"></div><h3>Totally Flexible</h3><p>get the cloud you want and the latest innovations you need</p></article>
  <article class="card" style="left:57px;top:1282px"><div class="ico" role="img" aria-label="Value coin icon"></div><h3>Greater Value For Money</h3><p>totally transparent pricing for no nasty month-end surprises</p></article>
  <article class="card" style="left:334px;top:1282px"><div class="ico" role="img" aria-label="Deal tag icon"></div><h3>No Consultancy Fees</h3><p>we'll work with you and charge set fees for everything</p></article>
  <article class="card" style="left:612px;top:1282px"><div class="ico" role="img" aria-label="Monitoring dashboard icon"></div><h3>Management, Monitoring And Maintenance</h3><p>they're all included in your monthly price</p></article>
  <article class="card" style="left:891px;top:1282px"><div class="ico" role="img" aria-label="Tested solution box icon"></div><h3>Tried And Tested Solutions</h3><p>we'll deploy the right OpenStratum solutions for your business</p></article>
</section>

<section class="transform">
  <div class="accent" style="left:57px;top:128px"></div>
  <h2>CHAAS Can Drive Your Digital Transformation Today</h2>
  <div class="copy">
    <p>Organisations of all shapes and sizes are reaping the time and money saving benefits that the cloud brings</p>
    <p>But for small businesses seeking to transition, managing the time and financial costs of transitioning, and knowing whether to opt for a public or private cloud can cause you to hit the pause button</p>
    <p>CHAAS is here to help you switch on your cloud transformation in a way that works best for you. We deliver and support fully managed private cloud solutions that are:</p>
  </div>
  <div class="check" style="left:57px;top:552px"><svg viewBox="0 0 20 20"><circle cx="10" cy="10" r="10" fill="#1d86d6"/><path d="M5.5 10.5l3 3 6-6.5" stroke="#fff" stroke-width="2" fill="none"/></svg>Fast</div>
  <div class="check" style="left:303px;top:552px"><svg viewBox="0 0 20 20"><circle cx="10" cy="10" r="10" fill="#1d86d6"/><path d="M5.5 10.5l3 3 6-6.5" stroke="#fff" stroke-width="2" fill="none"/></svg>Powerful</div>
  <div class="check" style="left:57px;top:603px"><svg viewBox="0 0 20 20"><circle cx="10" cy="10" r="10" fill="#1d86d6"/><path d="M5.5 10.5l3 3 6-6.5" stroke="#fff" stroke-width="2" fill="none"/></svg>Easy</div>
  <div class="check" style="left:303px;top:603px"><svg viewBox="0 0 20 20"><circle cx="10" cy="10" r="10" fill="#1d86d6"/><path d="M5.5 10.5l3 3 6-6.5" stroke="#fff" stroke-width="2" fill="none"/></svg>Scalable</div>
  <a class="btn" style="left:57px;top:679px;width:170px;height:52px" href="#">Get Started</a>
  <a class="link" style="left:280px;top:693px" href="#">Learn more<svg width="18" height="12" viewBox="0 0 18 12"><path d="M0 6h16M11 1l5 5-5 5" stroke="#f7931e" stroke-width="1.6" fill="none"/></svg></a>
  <div class="art" role="img" aria-label="Isometric illustration of server racks uploading to a cloud" style="left:658px;top:90px;width:480px;height:656px;background:radial-gradient(ellipse at 60% 20%,#cfe6f8 0%,rgba(10,29,41,0) 30%),radial-gradient(ellipse at 50% 60%,#2e7fcb 0%,#16406a 42%,rgba(10,29,41,0) 72%)"></div>
</section>

<section class="public">
  <div class="accent" style="left:57px;top:2551px"></div>
  <h2>If You're Using A Public Cloud Now</h2>
  <article class="pcard" style="left:57px;top:2703px;height:210px"><div class="head"><div class="pico" role="img" aria-label="Functionality icon"></div><h3>You're Likely Not Getting The Benefits Of Full Functionality</h3></div><p>Public cloud providers cannot adopt new innovations and functions as quickly and easily as the private cloud solutions you'll get from CHAAS</p></article>
  <article class="pcard" style="left:620px;top:2557px;height:206px"><div class="head"><div class="pico green" role="img" aria-label="Pricing icon"></div><h3>You Could Be Paying Too Much</h3></div><p>Public cloud pricing structures have a habit of sneakily scaling up very quickly</p><p style="margin-top:4px">With CHAAS, you'll always know what you're paying for your private cloud services</p></article>
  <article class="pcard" style="left:620px;top:2799px;height:206px"><div class="head"><div class="pico blue" role="img" aria-label="Linked services icon"></div><h3>You'll Be Tied To The Services Your Provider Can Provide</h3></div><p>Public cloud providers will have a limited suite of products and services to offer you</p><p style="margin-top:10px">A CHAAS private cloud has no such limitations</p></article>
  <div class="outline">Get Started</div>
</section>

<section class="diff">
  <div class="accent" style="left:57px;top:72px"></div>
  <h2>What Makes CHAAS Different</h2>
  <a class="btn" style="left:950px;top:108px;width:191px;height:52px" href="#">Pick Your Plan</a>
  <div class="step" style="left:102px;top:217px"><div class="num">1</div><p>We'll quickly get to grips with what your organisation needs, and deliver it via our private cloud solutions</p></div>
  <div class="step" style="left:102px;top:333px"><div class="num">2</div><p>Managed operations from private OpenStratum clouds and Kubeline</p></div>
  <div class="step" style="left:102px;top:449px"><div class="num">3</div><p>You can focus on your core business while we support you with a dedicated cloud infrastructure</p></div>
  <div class="step" style="left:102px;top:568px"><div class="num">4</div><p>Fast and easy computing, storage and network resources</p></div>
  <div class="step" style="left:654px;top:217px"><div class="num">5</div><p>We'll create and deliver the launchpad that will take your business forward</p></div>
  <div class="step" style="left:654px;top:333px"><div class="num">6</div><p>Get the benefits of your own cloud infrastructure and reduce your operational costs</p></div>
  <div class="step" style="left:654px;top:449px"><div class="num">7</div><p>Enjoy the ease of the public cloud, combined with the features, innovations and flexibility of the private cloud</p></div>
  <div class="step" style="left:654px;top:568px"><div class="num">8</div><p>We'll support your growth and scale your cloud as you need it</p></div>
</section>
<svg class="abs" style="left:0;top:3900px" width="1200" height="240" viewBox="0 0 1200 240" aria-hidden="true">
  <rect width="1200" height="240" fill="#ffffff"/>
  <polygon points="0,0 1200,0 1200,100 600,120 0,40" fill="#0a1d29"/>
  <polygon points="0,40 600,120 0,150" fill="#5b86a7"/>
  <polygon points="0,150 600,120 1200,100 1200,130 0,220" fill="#bcd8ec"/>
  <polygon points="0,40 420,95 0,110" fill="#7ea6c4"/>
</svg>

<section class="news">
  <div class="bar"></div>
  <h2>Join Our Newsletter</h2>
  <p>Join Now And Recieve E-Mail Updates On New Solutions And Services, Special Promotions, New Deals And More</p>
  <div class="field">Enter Your Email</div>
  <a class="btn" style="left:797px;top:4302px;width:153px;height:55px" href="#">Join Now</a>
</section>

<footer class="footer">
  <div class="logo" style="left:57px;top:80px"><span class="dot"></span>Cloudharborly</div>
  <p class="about">Cloudharborly as a Service is here to help small businesses utilise the power of the cloud without complicated set-ups or scary price tags</p>
  <span class="social" style="left:57px"></span><span class="social" style="left:100px"></span><span class="social" style="left:143px"></span>
  <div class="col" style="left:404px"><h4>Navigation</h4><ul><li>Home</li><li>Products</li><li>Solutions</li><li>Pricing</li><li>About Us</li></ul></div>
  <div class="col" style="left:557px"><h4>Support</h4><ul><li>FAQs</li><li>Customer Support</li><li>Help</li><li>Request a Demo</li></ul></div>
  <div class="col" style="left:750px"><h4>Company</h4><ul><li>Leadership</li><li>Newsroom</li><li>Customers</li><li>Partners</li><li>Careers</li></ul></div>
  <div class="col" style="left:849px"><h4>Contact Us</h4><ul>
    <li class="c"><svg viewBox="0 0 12 12"><path d="M2.5 1l2 2.5-1.2 1.3a7 7 0 003.9 3.9L8.5 7.5 11 9.5 10 11C5 11 1 7 1 2z" fill="#fff"/></svg>+1 555 014 2288</li>
    <li class="c"><svg viewBox="0 0 12 12"><path d="M2.5 1l2 2.5-1.2 1.3a7 7 0 003.9 3.9L8.5 7.5 11 9.5 10 11C5 11 1 7 1 2z" fill="#fff"/></svg>+1 555 014 2291</li>
    <li class="c"><svg viewBox="0 0 12 12"><rect x="1" y="2.5" width="10" height="7" fill="#fff"/><path d="M1 3l5 3.5L11 3" stroke="#0a1d29" fill="none"/></svg>hello@cloudharborly.com</li>
  </ul></div>
  <div class="rule"></div>
  <div class="copyright"><svg width="16" height="16" viewBox="0 0 16 16"><circle cx="8" cy="8" r="7" stroke="#fff" fill="none"/><path d="M10.5 6a3 3 0 100 4" stroke="#fff" fill="none"/></svg>2022 Cloudharborly Services</div>
  <div class="legal">Privacy Policy &nbsp;|&nbsp; Terms Of Service</div>
</footer>

</body>
</html>
```